A farm is looking for the unified design for the bags' and bottles' labels in their organic produ...

We are a farm that deals with the production and sale of the organic seeds and oils. From the seed programme, we offer the organic flax, sunflower, hemp and pumpkin seeds. In our program, the organic unrefined cold-pressed hemp, linseed and sunflower oil and cold-pressed pumpkin oil can be found.
Design wise, we want to unify our sales programme with a unique organic look of bottle labels containing organic oils and labels for paper bags containing seeds.
We intend to keep the appearance of the exiting logotype (refer to the logotype provided in the enclosed PDF file). Regarding the colours, our products should be separated by a colour scheme (hemp, flax, pumpkin seeds, sunflower, etc.). The label material should be the same for the bags and the bottles. If possible, we would like to utilize the ecological paper, together with the option of applying the labels using the organic glue (starch, etc.). Also, the possibility of the eventual later printing directly onto the packaging (paper bags and bottles) must be considered and envisioned.
Additionally, there should be space on the label for the written title of the product (for example, »BIO pumpkin seeds«) and some space for short indications, markings and data in the corners of the label. You can also include an image that will indicate the contents of the bag/bottle.
We will appreciate all your contributions.

IN DOMESTIC LANGUAGE:
Smo kmetija, ki se ukvarja s pridelavo in prodajo ekoloških semen in olj. Iz programa semen nudimo BIO lanena, sončnična, konopljina in bučna semena. V našem programu so BIO nerafinirano hladno stiskano konopljino, laneno ter sončnično olje in hladno stiskano bučno olje.
Želimo oblikovno poenotiti naš prodajni program z enotnim EKO videzom etiket za steklenice z BIO olji in etiket za papirnate vrečke z semeni.
Ohraniti nameravamo videz obstoječega logotipa (glej logotip v priloženi PDF datoteki). Barvno je treba ločiti proizvode po barvni shemi (konoplja, lan, bučno seme, sončnica …). Material etiket naj bo enak za vrečke in steklenice. Po možnosti naj gre za ekološki papir, pa tudi možnost nanosa etiket z ekološkim lepilom (škrob …). Predvideti je treba tudi možen kasnejši tisk neposredno na embalažo (papirnate vrečke ter steklenice).
Prav tako naj bo na etiketi prostor za napis naslova izdelka (na primer »BIO bučno seme«) in po robovih nekaj prostora za krajše navedbe, označbe ter podatke, vključena pa je lahko tudi slika, ki nakazuje na vsebino vrečke/steklenice.
Najlepša hvala že vnaprej za vaše prispevke.

```html
<!DOCTYPE html>
<html lang="en">
<head>
<meta charset="utf-8">
<title>Organic Oils – Label System</title>
<link rel="stylesheet" href="https://fonts.googleapis.com/css2?family=Didact+Gothic&display=swap">
<style>
  :root {
    --page: #ffffff;
    --panel-line: #a9a9a9;
    --ink: #2b2b22;
    --arrow: #111111;
    --frame: #ffffff;

    --linseed-light: #f3dfba;
    --linseed-edge: #e2bd86;
    --linseed-accent: #6a1812;
    --linseed-photo: #b39455;

    --sunflower-light: #fbe676;
    --sunflower-edge: #f2bf16;
    --sunflower-accent: #036737;
    --sunflower-photo: #c8c294;

    --hemp-light: #b7dc7a;
    --hemp-edge: #74b43b;
    --hemp-accent: #026534;
    --hemp-photo: #e3e8dc;

    --pumpkin-light: #ffd064;
    --pumpkin-edge: #fba60c;
    --pumpkin-accent: #d65a00;
    --pumpkin-photo: #c9a56c;
  }
  * { box-sizing: border-box; margin: 0; padding: 0; }
  html, body { width: 1200px; height: 999px; overflow: hidden; background: var(--page); }
  .board { position: relative; width: 1200px; height: 999px; font-family: "Didact Gothic", sans-serif; color: var(--ink); }

  .overview-panel { position: absolute; left: 0; top: 0; }

  .label { position: absolute; }
  .label__paper {
    position: absolute; inset: 0;
    border-radius: var(--r) var(--r) 0 0;
    background: radial-gradient(ellipse at 50% 45%, var(--light) 0%, var(--light) 35%, var(--edge) 100%);
  }
  .label__art { position: absolute; inset: 0; width: 100%; height: 100%; overflow: visible; }
  .label--large { width: 315px; height: 439px; --r: 40px; }
  .label--mini-lg { width: 160px; height: 223px; --r: 20px; }
  .label--mini-sm { width: 128px; height: 178px; --r: 16px; }

  .label--linseed   { --light: var(--linseed-light);   --edge: var(--linseed-edge);   --accent: var(--linseed-accent);   --photo: var(--linseed-photo); }
  .label--sunflower { --light: var(--sunflower-light); --edge: var(--sunflower-edge); --accent: var(--sunflower-accent); --photo: var(--sunflower-photo); }
  .label--hemp      { --light: var(--hemp-light);      --edge: var(--hemp-edge);      --accent: var(--hemp-accent);      --photo: var(--hemp-photo); }
  .label--pumpkin   { --light: var(--pumpkin-light);   --edge: var(--pumpkin-edge);   --accent: var(--pumpkin-accent);   --photo: var(--pumpkin-photo); }

  .accent { fill: var(--accent); }
  .frame-line { fill: none; stroke: var(--frame); stroke-width: 2.2; }
  .title-rule { stroke: var(--accent); stroke-width: 1; }
  .title-text { font-family: "Didact Gothic", sans-serif; font-size: 11px; fill: var(--ink); text-anchor: middle; letter-spacing: 0.2px; }
  .hex-border { fill: var(--frame); stroke: var(--frame); stroke-width: 12; stroke-linejoin: round; }
  .hex-photo { fill: var(--photo); }

  .callout { position: absolute; font-size: 22px; line-height: 26px; text-align: center; color: var(--ink); }
  .callouts { position: absolute; left: 0; top: 0; }
</style>
</head>
<body>
<main class="board">

  <svg class="overview-panel" width="760" height="500" viewBox="0 0 760 500" aria-hidden="true">
    <path d="M0 497 H708 A40 40 0 0 0 748 457 V0" fill="none" stroke="var(--panel-line)" stroke-width="3"/>
  </svg>

  <!-- Overview labels -->
  <div class="label label--mini-sm label--linseed" style="left:105px; top:283px;">
    <div class="label__paper"></div>
    <svg class="label__art" viewBox="0 0 315 439" preserveAspectRatio="none">
      <path class="frame-line" d="M14 439 V40 A14 14 0 0 0 28 26 V14 H287 V26 A14 14 0 0 0 301 40 V439"/>
      <path class="accent" d="M105 0 H211 V40 A12 12 0 0 1 199 52 H117 A12 12 0 0 1 105 40 Z"/>
      <line class="title-rule" x1="78" y1="66" x2="237" y2="66"/><line class="title-rule" x1="78" y1="84" x2="237" y2="84"/>
      <text class="title-text" x="157.5" y="79">ORGANIC LINSEED OIL</text>
      <path class="hex-border" d="M157.5 110 L258 162 V298 L157.5 348 L57 298 V162 Z"/>
      <path class="hex-photo" role="img" aria-label="Photo of flax plants, linseed and a glass of linseed oil" d="M157.5 116 L252 165 V295 L157.5 342 L63 295 V165 Z"/>
      <path class="accent" d="M35 283 H280 L266 304 L280 325 H35 L49 304 Z"/>
      <path class="accent" d="M0 394 H100 V384 A13 13 0 0 1 113 371 H202 A13 13 0 0 1 215 384 V394 H315 V439 H0 Z"/>
      <path class="frame-line" d="M0 401 H108 V389 A8 8 0 0 1 116 381 H199 A8 8 0 0 1 207 389 V401 H315"/>
      <path class="frame-line" d="M14 401 V439 M301 401 V439"/>
    </svg>
  </div>

  <div class="label label--mini-lg label--sunflower" style="left:262px; top:232px;">
    <div class="label__paper"></div>
    <svg class="label__art" viewBox="0 0 315 439" preserveAspectRatio="none">
      <path class="frame-line" d="M14 439 V40 A14 14 0 0 0 28 26 V14 H287 V26 A14 14 0 0 0 301 40 V439"/>
      <path class="accent" d="M105 0 H211 V40 A12 12 0 0 1 199 52 H117 A12 12 0 0 1 105 40 Z"/>
      <line class="title-rule" x1="78" y1="66" x2="237" y2="66"/><line class="title-rule" x1="78" y1="84" x2="237" y2="84"/>
      <text class="title-text" x="157.5" y="79">ORGANIC SUNFLOWER OIL</text>
      <path class="hex-border" d="M157.5 110 L258 162 V298 L157.5 348 L57 298 V162 Z"/>
      <path class="hex-photo" role="img" aria-label="Photo of sunflowers beside a bottle of sunflower oil" d="M157.5 116 L252 165 V295 L157.5 342 L63 295 V165 Z"/>
      <path class="accent" d="M35 283 H280 L266 304 L280 325 H35 L49 304 Z"/>
      <path class="accent" d="M0 394 H100 V384 A13 13 0 0 1 113 371 H202 A13 13 0 0 1 215 384 V394 H315 V439 H0 Z"/>
      <path class="frame-line" d="M0 401 H108 V389 A8 8 0 0 1 116 381 H199 A8 8 0 0 1 207 389 V401 H315"/>
      <path class="frame-line" d="M14 401 V439 M301 401 V439"/>
    </svg>
  </div>

  <svg class="callouts" width="760" height="500" viewBox="0 0 760 500" aria-hidden="true">
    <defs>
      <marker id="arrowhead" viewBox="0 0 10 10" refX="8" refY="5" markerWidth="9" markerHeight="9" orient="auto">
        <path d="M1 1 L8 5 L1 9" fill="none" stroke="var(--arrow)" stroke-width="1.6"/>
      </marker>
    </defs>
    <path d="M345 243 C380 200 440 182 505 181" fill="none" stroke="var(--arrow)" stroke-width="2" marker-end="url(#arrowhead)"/>
    <path d="M350 387 C395 355 450 337 505 334" fill="none" stroke="var(--arrow)" stroke-width="2" marker-end="url(#arrowhead)"/>
    <path d="M362 440 C410 455 460 440 500 426" fill="none" stroke="var(--arrow)" stroke-width="2" marker-end="url(#arrowhead)"/>
  </svg>
  <p class="callout" style="left:505px; top:167px; width:190px;">Your Brand Logo<br>Here</p>
  <p class="callout" style="left:500px; top:309px; width:160px;">Title of<br>the Product</p>
  <p class="callout" style="left:495px; top:395px; width:205px;">Short Information<br>or Data</p>

  <!-- Full-size labels -->
  <div class="label label--large label--linseed" style="left:825px; top:38px;">
    <div class="label__paper"></div>
    <svg class="label__art" viewBox="0 0 315 439">
      <path class="frame-line" d="M14 439 V40 A14 14 0 0 0 28 26 V14 H287 V26 A14 14 0 0 0 301 40 V439"/>
      <path class="accent" d="M105 0 H211 V40 A12 12 0 0 1 199 52 H117 A12 12 0 0 1 105 40 Z"/>
      <line class="title-rule" x1="78" y1="66" x2="237" y2="66"/><line class="title-rule" x1="78" y1="84" x2="237" y2="84"/>
      <text class="title-text" x="157.5" y="79">ORGANIC LINSEED OIL</text>
      <path class="hex-border" d="M157.5 110 L258 162 V298 L157.5 348 L57 298 V162 Z"/>
      <path class="hex-photo" role="img" aria-label="Photo of flax plants, linseed and a glass of linseed oil" d="M157.5 116 L252 165 V295 L157.5 342 L63 295 V165 Z"/>
      <path class="accent" d="M35 283 H280 L266 304 L280 325 H35 L49 304 Z"/>
      <path class="accent" d="M0 394 H100 V384 A13 13 0 0 1 113 371 H202 A13 13 0 0 1 215 384 V394 H315 V439 H0 Z"/>
      <path class="frame-line" d="M0 401 H108 V389 A8 8 0 0 1 116 381 H199 A8 8 0 0 1 207 389 V401 H315"/>
      <path class="frame-line" d="M14 401 V439 M301 401 V439"/>
    </svg>
  </div>

  <div class="label label--large label--sunflower" style="left:60px; top:522px;">
    <div class="label__paper"></div>
    <svg class="label__art" viewBox="0 0 315 439">
      <path class="frame-line" d="M14 439 V40 A14 14 0 0 0 28 26 V14 H287 V26 A14 14 0 0 0 301 40 V439"/>
      <path class="accent" d="M105 0 H211 V40 A12 12 0 0 1 199 52 H117 A12 12 0 0 1 105 40 Z"/>
      <line class="title-rule" x1="78" y1="66" x2="237" y2="66"/><line class="title-rule" x1="78" y1="84" x2="237" y2="84"/>
      <text class="title-text" x="157.5" y="79">ORGANIC SUNFLOWER OIL</text>
      <path class="hex-border" d="M157.5 110 L258 162 V298 L157.5 348 L57 298 V162 Z"/>
      <path class="hex-photo" role="img" aria-label="Photo of sunflowers beside a bottle of sunflower oil" d="M157.5 116 L252 165 V295 L157.5 342 L63 295 V165 Z"/>
      <path class="accent" d="M35 283 H280 L266 304 L280 325 H35 L49 304 Z"/>
      <path class="accent" d="M0 394 H100 V384 A13 13 0 0 1 113 371 H202 A13 13 0 0 1 215 384 V394 H315 V439 H0 Z"/>
      <path class="frame-line" d="M0 401 H108 V389 A8 8 0 0 1 116 381 H199 A8 8 0 0 1 207 389 V401 H315"/>
      <path class="frame-line" d="M14 401 V439 M301 401 V439"/>
    </svg>
  </div>

  <div class="label label--large label--hemp" style="left:443px; top:522px;">
    <div class="label__paper"></div>
    <svg class="label__art" viewBox="0 0 315 439">
      <path class="frame-line" d="M14 439 V40 A14 14 0 0 0 28 26 V14 H287 V26 A14 14 0 0 0 301 40 V439"/>
      <path class="accent" d="M105 0 H211 V40 A12 12 0 0 1 199 52 H117 A12 12 0 0 1 105 40 Z"/>
      <line class="title-rule" x1="78" y1="66" x2="237" y2="66"/><line class="title-rule" x1="78" y1="84" x2="237" y2="84"/>
      <text class="title-text" x="157.5" y="79">ORGANIC UNREFINED COLD-PRESSED HEMP</text>
      <path class="hex-border" d="M157.5 110 L258 162 V298 L157.5 348 L57 298 V162 Z"/>
      <path class="hex-photo" role="img" aria-label="Photo of hemp leaves beside a bottle of hemp oil" d="M157.5 116 L252 165 V295 L157.5 342 L63 295 V165 Z"/>
      <path class="accent" d="M35 283 H280 L266 304 L280 325 H35 L49 304 Z"/>
      <path class="accent" d="M0 394 H100 V384 A13 13 0 0 1 113 371 H202 A13 13 0 0 1 215 384 V394 H315 V439 H0 Z"/>
      <path class="frame-line" d="M0 401 H108 V389 A8 8 0 0 1 116 381 H199 A8 8 0 0 1 207 389 V401 H315"/>
      <path class="frame-line" d="M14 401 V439 M301 401 V439"/>
    </svg>
  </div>

  <div class="label label--large label--pumpkin" style="left:825px; top:522px;">
    <div class="label__paper"></div>
    <svg class="label__art" viewBox="0 0 315 439">
      <path class="frame-line" d="M14 439 V40 A14 14 0 0 0 28 26 V14 H287 V26 A14 14 0 0 0 301 40 V439"/>
      <path class="accent" d="M105 0 H211 V40 A12 12 0 0 1 199 52 H117 A12 12 0 0 1 105 40 Z"/>
      <line class="title-rule" x1="78" y1="66" x2="237" y2="66"/><line class="title-rule" x1="78" y1="84" x2="237" y2="84"/>
      <text class="title-text" x="157.5" y="79">ORGANIC COLD-PRESSED PUMPKIN OIL</text>
      <path class="hex-border" d="M157.5 110 L258 162 V298 L157.5 348 L57 298 V162 Z"/>
      <path class="hex-photo" role="img" aria-label="Photo of pumpkin seeds beside a bottle of pumpkin oil" d="M157.5 116 L252 165 V295 L157.5 342 L63 295 V165 Z"/>
      <path class="accent" d="M35 283 H280 L266 304 L280 325 H35 L49 304 Z"/>
      <path class="accent" d="M0 394 H100 V384 A13 13 0 0 1 113 371 H202 A13 13 0 0 1 215 384 V394 H315 V439 H0 Z"/>
      <path class="frame-line" d="M0 401 H108 V389 A8 8 0 0 1 116 381 H199 A8 8 0 0 1 207 389 V401 H315"/>
      <path class="frame-line" d="M14 401 V439 M301 401 V439"/>
    </svg>
  </div>

</main>
</body>
</html>
```